Zanquorra Business Card Design

Zanquorra is a small and new restaurant/ bar location in Hong Kong. The name "Djibouti" derives from an African country. There is no specific reason behind other than the fact, that the bar is somewhat inspired by African elements (only inspired but not purely based on African cuisine etc.).

The bar is somewhat a fusion of African, Mediterranean and Oriental (Old French Vietnam) elements.

However, it is very imperative to stress, that the overall look and feel of Zanquorra is a very high end cocktail lounge/ bar location. The bar is tucked away in a hidden alley, so people will have to know about it. The idea is to send the consumer off in an Escape or hidden remote location where they are at ease in a hip, stylish and trendy environment.

The card needs to feel high-end.

Final logo artwork has been attached and also pictures of the bar/ restaurant itself. The logo ie monkey head cannot be modified. However, the background color and the color of the type "ZANQUORRA" can be changed.

The following details need to fit onto the business card. Of course they can be arranged to your liking:

LOGO

Colin Vey
Partner

+852 97035164
xxx@zanquorra.com
www.zanquorra.com
7C, Brennick Road, Wan Chai, Hong Kong

```html
<!DOCTYPE html>
<html lang="en">
<head>
<meta charset="UTF-8">
<title>Zanquorra Business Card</title>
<link rel="stylesheet" href="https://fonts.googleapis.com/css2?family=Ubuntu:wght@400;500;700&display=swap">
<style>
  :root {
    --page: #d9d9d7;
    --ink-dark: #231c10;
    --card-white: #f1f1ef;
    --text-light: #e6e4df;
    --text-grey: #5a5650;
    --crimson: #b0123a;
    --red: #d6163f;
    --orange: #e07a12;
    --yellow: #f0b50f;
    --cyan: #10a4dd;
    --blue: #0a6fba;
    --navy: #1f3a8a;
  }
  * { margin: 0; padding: 0; box-sizing: border-box; }
  html, body {
    width: 1200px; height: 1000px; overflow: hidden;
    background: var(--page);
    font-family: "Ubuntu", sans-serif;
  }
  .canvas { position: relative; width: 1200px; height: 1000px; }
  .card {
    position: absolute; left: 250px; width: 700px; height: 400px;
    overflow: hidden; box-shadow: 0 6px 18px rgba(0,0,0,0.18);
  }
  .card-back { top: 70px; background: var(--ink-dark); }
  .card-front { top: 530px; background: var(--card-white); }

  .spectrum { position: absolute; display: flex; }
  .spectrum span { flex: 1; }
  .spectrum .s1 { background: var(--crimson); }
  .spectrum .s2 { background: var(--red); }
  .spectrum .s3 { background: var(--orange); }
  .spectrum .s4 { background: var(--yellow); }
  .spectrum .s5 { background: var(--cyan); }
  .spectrum .s6 { background: var(--blue); }
  .spectrum .s7 { background: var(--navy); }

  .card-back .spectrum { left: 0; top: 224px; width: 400px; height: 13px; }

  .brand { position: absolute; text-align: center; }
  .brand-mark {
    display: block; margin: 0 auto 12px; border-radius: 50%;
  }
  .brand-name {
    font-weight: 500; letter-spacing: 2px; font-size: 24px; display: block;
  }
  .card-back .brand { left: 440px; top: 150px; width: 220px; }
  .card-back .brand-mark { width: 80px; height: 80px; border: 3px solid var(--text-light); }
  .card-back .brand-name { color: var(--text-light); }

  .card-front .brand { left: 40px; top: 36px; width: 170px; }
  .card-front .brand-mark { width: 68px; height: 68px; border: 3px solid var(--ink-dark); }
  .card-front .brand-name { color: var(--ink-dark); font-size: 21px; }

  .card-front .spectrum { left: 0; top: 196px; width: 700px; height: 16px; }
  .info-band { position: absolute; left: 0; top: 212px; width: 700px; height: 120px; background: var(--ink-dark); }
  .name-tab { position: absolute; left: 0; top: 0; }
  .person { position: absolute; left: 520px; top: 152px; color: var(--text-light); }
  .person-name { font-weight: 700; font-size: 22px; line-height: 1; }
  .person-role { font-size: 14px; margin-top: 3px; }

  .contact { position: absolute; color: var(--text-light); font-size: 16px; text-align: center; }
  .contact svg { display: block; margin: 0 auto 10px; }
  .contact-phone { left: 30px; top: 232px; width: 170px; }
  .contact-email { left: 240px; top: 245px; width: 200px; }
  .contact-web { left: 470px; top: 258px; width: 200px; font-weight: 500; }
  .address { position: absolute; left: 40px; top: 352px; color: var(--text-grey); font-size: 17px; }
</style>
</head>
<body>
<main class="canvas">

  <section class="card card-back" aria-label="Card back">
    <div class="spectrum"><span class="s1"></span><span class="s2"></span><span class="s3"></span><span class="s4"></span><span class="s5"></span><span class="s6"></span><span class="s7"></span></div>
    <div class="brand">
      <span class="brand-mark"></span>
      <span class="brand-name">ZANQUORRA</span>
    </div>
  </section>

  <section class="card card-front" aria-label="Card front">
    <div class="brand">
      <span class="brand-mark"></span>
      <span class="brand-name">ZANQUORRA</span>
    </div>

    <svg class="name-tab" width="700" height="212" viewBox="0 0 700 212" aria-hidden="true">
      <polygon points="470,148 700,148 700,196 430,196" fill="var(--ink-dark)"/>
    </svg>
    <div class="spectrum"><span class="s1"></span><span class="s2"></span><span class="s3"></span><span class="s4"></span><span class="s5"></span><span class="s6"></span><span class="s7"></span></div>
    <div class="info-band"></div>

    <div class="person">
      <div class="person-name">Colin Vey</div>
      <div class="person-role">Partner</div>
    </div>

    <div class="contact contact-phone">
      <svg width="18" height="18" viewBox="0 0 24 24" aria-hidden="true"><path fill="var(--text-light)" d="M6.6 2.5 9.4 6.8 7.6 9c1.3 2.8 4.2 5.7 7.4 7.4l2.2-1.8 4.3 2.8-1.4 4.1C12 21.2 2.8 12 2.5 3.9z"/></svg>
      +852 97035164
    </div>
    <div class="contact contact-email">
      <svg width="24" height="18" viewBox="0 0 24 18" aria-hidden="true"><rect x="1" y="1" width="22" height="16" fill="none" stroke="var(--text-light)" stroke-width="2"/><path d="M1 1 12 10 23 1" fill="none" stroke="var(--text-light)" stroke-width="2"/></svg>
      xxx@zanquorra.com
    </div>
    <div class="contact contact-web">
      <svg width="22" height="22" viewBox="0 0 24 24" aria-hidden="true"><g fill="none" stroke="var(--text-light)" stroke-width="2"><circle cx="12" cy="12" r="10"/><ellipse cx="12" cy="12" rx="4.5" ry="10"/><path d="M2 12h20"/></g></svg>
      www.zanquorra.com
    </div>

    <div class="address">7C, Brennick Road, Wan Chai, Hong Kong</div>
  </section>

</main>
</body>
</html>
```